Brightlane Photography
Sports & Dance Photography
Brightlane Photography - Photography
Creative Brief
Photography
Sports Leagues and Dance Schools
I have included an old brocure for sme reference material on our services. I would like trifold format
Marcotoledo Marcotoledo
Please download the asset file

```html
<!DOCTYPE html>
<html lang="en">
<head>
<meta charset="utf-8">
<title>Brightlane Photography – Trifold Inside Spread</title>
<link rel="stylesheet" href="https://fonts.googleapis.com/css2?family=Montserrat:wght@700;800&family=Open+Sans:wght@400;600&display=swap">
<style>
  :root {
    --page-bg: #e4e5e7;
    --paper: #ffffff;
    --ink: #2b2b2e;
    --body-ink: #5a5b60;
    --magenta: #e6197d;
    --green: #3fb44a;
    --teal: #25b8ae;
    --orange: #f5a21b;
    --photo-dark: #2a2a33;
    --photo-red: #7a2431;
    --photo-blue: #2d3d6e;
    --photo-warm: #8a6a52;
    --fold: rgba(0,0,0,0.07);
  }
  * { box-sizing: border-box; margin: 0; padding: 0; }
  html, body { width: 1200px; height: 799px; overflow: hidden; }
  body {
    background: var(--page-bg);
    font-family: "Open Sans", Arial, sans-serif;
    display: flex; align-items: center; justify-content: center;
  }
  .brochure {
    width: 960px; height: 742px;
    background: var(--paper);
    display: grid; grid-template-columns: repeat(3, 1fr);
    box-shadow: 0 10px 30px rgba(0,0,0,0.18);
  }
  .panel {
    display: grid; grid-template-rows: 1fr 1fr;
    border-right: 1px solid var(--fold);
    overflow: hidden;
  }
  .panel:last-child { border-right: none; }
  .service {
    display: flex; flex-direction: column;
    padding-top: 18px;
  }
  .service-question {
    font-family: "Montserrat", Arial, sans-serif;
    font-weight: 800; font-size: 12.5px; line-height: 1.3;
    color: var(--ink); text-transform: uppercase; text-align: center;
    padding: 0 26px; min-height: 34px;
  }
  .service-ribbon {
    position: relative; margin: 10px 0 10px 0;
    height: 30px; display: flex; align-items: center;
    padding-left: 62px;
    font-family: "Montserrat", Arial, sans-serif;
    font-weight: 800; font-size: 15px; color: #fff;
    text-transform: uppercase; letter-spacing: 0.3px;
  }
  .service-ribbon::before {
    content: ""; position: absolute; left: 22px; right: 40px; top: 0; bottom: 0;
    background: var(--accent); z-index: 0;
    clip-path: polygon(0 0, 100% 0, 94% 100%, 0 100%);
  }
  .service-ribbon span { position: relative; z-index: 1; }
  .ribbon-icon {
    position: absolute; left: 14px; top: -5px; z-index: 2;
    width: 40px; height: 40px; border-radius: 50%;
    background: var(--accent); border: 3px solid #fff;
    box-shadow: 0 1px 3px rgba(0,0,0,0.2);
    display: flex; align-items: center; justify-content: center;
  }
  .ribbon-icon svg { width: 20px; height: 20px; }
  .accent-magenta { --accent: var(--magenta); }
  .accent-green { --accent: var(--green); }
  .accent-teal { --accent: var(--teal); }
  .accent-orange { --accent: var(--orange); }
  .service-text {
    font-size: 9.5px; line-height: 1.55; color: var(--body-ink);
    padding: 0 24px; text-align: left;
  }
  .service-photo {
    margin-top: auto; height: 150px; width: 100%;
  }
  .photo-team-red { background: linear-gradient(160deg, var(--photo-red), var(--photo-dark)); }
  .photo-display { background: linear-gradient(160deg, var(--photo-warm), var(--photo-dark)); }
  .photo-team-field { background: linear-gradient(170deg, #9aa3a0, #3b4a3a); }
  .photo-dance { background: linear-gradient(160deg, var(--photo-blue), #141828); }
  .photo-athlete { background: linear-gradient(120deg, var(--photo-red), #151515 70%); }
  .product-row {
    display: flex; gap: 12px; padding: 0 20px; align-items: flex-start;
  }
  .product-row .service-text { padding: 0; flex: 1; }
  .photo-products {
    width: 110px; height: 150px; flex: none;
    background: linear-gradient(150deg, #c33a4a, #2a2228);
  }
</style>
</head>
<body>
<main class="brochure">

  <section class="panel">
    <article class="service">
      <h2 class="service-question">Have you ever had lost orders or mistakes?</h2>
      <div class="service-ribbon accent-magenta">
        <div class="ribbon-icon"><svg viewBox="0 0 20 20" fill="none" stroke="#fff" stroke-width="2.4" stroke-linecap="round" stroke-linejoin="round"><path d="M4 10.5l4 4 8-9"/></svg></div>
        <span>Digital Ordering</span>
      </div>
      <p class="service-text">Every order is entered online by parents, checked by our team and matched to each player, so packages arrive right the first time with no lost forms or mixed up names.</p>
      <div class="service-photo photo-display" role="img" aria-label="Photo of a league picture day display table with sample prints"></div>
    </article>
    <article class="service">
      <h2 class="service-question">Have you been unable to make all your teams happy?</h2>
      <div class="service-ribbon accent-orange">
        <div class="ribbon-icon"><svg viewBox="0 0 20 20" fill="none" stroke="#fff" stroke-width="2" stroke-linecap="round"><rect x="3" y="4.5" width="14" height="12" rx="1.5"/><path d="M3 8.5h14M7 2.5v4M13 2.5v4"/></svg></div>
        <span>Online Scheduling</span>
      </div>
      <p class="service-text">Coaches pick their own picture day slots from a live calendar, so every team gets a time that fits practice and no one is left waiting in long lines.</p>
      <div class="service-photo photo-team-field" role="img" aria-label="Group photo of a youth sports team outdoors"></div>
    </article>
  </section>

  <section class="panel">
    <article class="service">
      <h2 class="service-question">Have you ever had bad customer service or been unable to get help?</h2>
      <div class="service-ribbon accent-green">
        <div class="ribbon-icon"><svg viewBox="0 0 20 20" fill="none" stroke="#fff" stroke-width="2" stroke-linecap="round"><circle cx="10" cy="10" r="7"/><path d="M10 6v4.5l3 2"/></svg></div>
        <span>24 Hour Helpdesk</span>
      </div>
      <p class="service-text">Our support team answers calls and messages day and night, helping parents with orders, coaches with rosters and league staff with anything they need during the season.</p>
      <div class="service-photo photo-team-red" role="img" aria-label="Group photo of a team in red uniforms in a gym"></div>
    </article>
    <article class="service">
      <h2 class="service-question">Do you still have photo packages left over from last season?</h2>
      <div class="service-ribbon accent-magenta">
        <div class="ribbon-icon"><svg viewBox="0 0 20 20" fill="none" stroke="#fff" stroke-width="2.2" stroke-linecap="round" stroke-linejoin="round"><path d="M3 10h13M11 5l5 5-5 5"/></svg></div>
        <span>Direct Shipping</span>
      </div>
      <p class="service-text">Prints are packed by player and shipped straight to each home, so leagues never sort boxes again and no unclaimed packages sit in a closet until next year.</p>
      <div class="service-photo photo-dance" role="img" aria-label="Group photo of a dance school troupe on stage"></div>
    </article>
  </section>

  <section class="panel">
    <article class="service">
      <h2 class="service-question">Can the people who take your amazing portraits make cool items for every person on your roster?</h2>
      <div class="service-ribbon accent-teal">
        <div class="ribbon-icon"><svg viewBox="0 0 20 20" fill="#fff"><path d="M10 2.5l2.3 4.9 5.2.6-3.9 3.6 1.1 5.2L10 14.2l-4.7 2.6 1.1-5.2L2.5 8l5.2-.6z"/></svg></div>
        <span>Awesome Products</span>
      </div>
      <div class="product-row">
        <div class="photo-products" role="img" aria-label="Photo of custom photo products such as banners and trading cards"></div>
        <p class="service-text">From banners and magnets to trading cards and keepsake frames, we turn every portrait into gear that players and families will love to show off.</p>
      </div>
    </article>
    <article class="service">
      <h2 class="service-question">Have you had a hard time finding a tournament photography expert?</h2>
      <div class="service-ribbon accent-orange">
        <div class="ribbon-icon"><svg viewBox="0 0 20 20" fill="none" stroke="#fff" stroke-width="2" stroke-linecap="round" stroke-linejoin="round"><path d="M6 3h8v4a4 4 0 0 1-8 0zM6 5H3.5a2.5 2.5 0 0 0 2.5 3M14 5h2.5a2.5 2.5 0 0 1-2.5 3M10 11v3M7 17h6M8 14h4"/></svg></div>
        <span>Tournaments</span>
      </div>
      <p class="service-text">Our crew covers full weekend events with action shots on every field, fast online galleries and on site printing so families can take memories home the same day.</p>
      <div class="service-photo photo-athlete" role="img" aria-label="Tournament portrait of a young athlete with a team name banner"></div>
    </article>
  </section>

</main>
</body>
</html>
```